Coral Wing Flights business card

I need a business card designed based on our logo -- designed by Pixel Guild designers.

The logo is to be taken from our web site at www.coralwingflights.com.au

I need to have this card designed quickly as its needed for business meetings
Updates

Hi Designers, Please see my updated brief for my business card. I have attached logo images and a brochure for inspiration... Regards, Marco Debellis Coral Wing Flights

Target Market(s)

Hotel owners and operators (concierge) and tourists to Australia

Industry/Entity Type

Business

Font styles to use
Sans Serif

Colors
84abd2
3176b5
85abd2
cedeec

Requirements
Must have
• Utilise our logo. Found on our web page www.coralwingflights.com.au

SIDE 1
Must have my name: Marco Debellis
Title:Owner
Phone number: 1300 418 295
Mobile:0431267589

SIDE 2
LOGO
PREPARE TO BE AMAZED! (see attached brochure for information and font style)
Nice to have
• Something that reflects aviation and tour with a light aircraft

```html
<!DOCTYPE html>
<html lang="en">
<head>
<meta charset="utf-8">
<title>Coral Wing Flights – Business Card</title>
<link rel="stylesheet" href="https://fonts.googleapis.com/css2?family=Open+Sans:wght@400;600&display=swap">
<style>
  :root {
    --brand-blue: #3f86cf;
    --brand-blue-deep: #3176b5;
    --brand-blue-soft: #84abd2;
    --brand-mist: #cedeec;
    --card-white: #f7fafd;
    --page-bg: #eceff2;
    --text-blue: #2f6fb3;
  }
  * { box-sizing: border-box; margin: 0; padding: 0; }
  html, body {
    width: 1200px;
    height: 675px;
    overflow: hidden;
    background: var(--page-bg);
    font-family: "Open Sans", Arial, sans-serif;
  }
  .canvas {
    position: relative;
    width: 1200px;
    height: 675px;
  }
  .card {
    position: absolute;
    top: 180px;
    width: 520px;
    height: 310px;
    overflow: hidden;
    box-shadow: 0 6px 18px rgba(0, 0, 0, 0.18);
  }

  /* Logo side */
  .card--logo {
    left: 50px;
    background: var(--brand-blue);
  }
  .card--logo .brand-name {
    position: absolute;
    top: 42px;
    right: 40px;
    color: #ffffff;
    font-size: 15px;
    font-weight: 600;
    letter-spacing: 0.5px;
    text-transform: uppercase;
  }
  .card--logo .plane-art {
    position: absolute;
    left: 150px;
    top: 88px;
    width: 220px;
    height: 140px;
    border-radius: 50%;
    background: radial-gradient(ellipse at center, rgba(255,255,255,0.85) 0%, rgba(255,255,255,0.35) 60%, rgba(255,255,255,0) 75%);
  }
  .card--logo .tagline {
    position: absolute;
    left: 0;
    right: 0;
    top: 252px;
    text-align: center;
    color: #ffffff;
    font-size: 14px;
    font-weight: 600;
    letter-spacing: 1.5px;
    text-transform: uppercase;
  }

  /* Details side */
  .card--details {
    left: 630px;
    background: radial-gradient(ellipse at 55% 40%, #ffffff 0%, var(--card-white) 45%, var(--brand-mist) 100%);
  }
  .card--details .block {
    position: absolute;
    left: 0;
    width: 150px;
    background: linear-gradient(135deg, var(--brand-blue-deep), var(--brand-blue));
  }
  .card--details .block--top { top: 0; height: 82px; }
  .card--details .block--bottom { bottom: 0; height: 100px; }
  .card--details .brand-name {
    position: absolute;
    left: 36px;
    top: 132px;
    color: var(--brand-blue-deep);
    font-size: 10px;
    font-weight: 600;
    letter-spacing: 0.4px;
    text-transform: uppercase;
  }
  .card--details .plane-art {
    position: absolute;
    left: 250px;
    top: 45px;
    width: 220px;
    height: 130px;
    border-radius: 50%;
    background: radial-gradient(ellipse at center, rgba(63,134,207,0.8) 0%, rgba(63,134,207,0.3) 60%, rgba(63,134,207,0) 75%);
  }
  .contact {
    position: absolute;
    left: 200px;
    top: 200px;
    display: grid;
    grid-template-columns: auto auto;
    column-gap: 8px;
    color: var(--text-blue);
    text-transform: uppercase;
    line-height: 1.2;
  }
  .contact dt { text-align: right; font-size: 14px; }
  .contact dd { font-size: 14px; }
  .contact .is-name { font-size: 19px; }
</style>
</head>
<body>
<main class="canvas">
  <section class="card card--logo" aria-label="Card logo side">
    <p class="brand-name">Coral Wing Flights</p>
    <div class="plane-art" role="img" aria-label="Light aircraft illustration with a curved flight path swoosh"></div>
    <p class="tagline">Prepare to be amazed!</p>
  </section>

  <section class="card card--details" aria-label="Card details side">
    <div class="block block--top"></div>
    <div class="block block--bottom"></div>
    <p class="brand-name">Coral Wing Flights</p>
    <div class="plane-art" role="img" aria-label="Light aircraft illustration with a curved flight path swoosh"></div>
    <dl class="contact">
      <dt class="is-name">Name :</dt><dd class="is-name">Marco Debellis</dd>
      <dt>Title :</dt><dd>Owner</dd>
      <dt>Contact :</dt><dd>1300 418 295</dd>
      <dt>Mobile :</dt><dd>0431267589</dd>
    </dl>
  </section>
</main>
</body>
</html>
```